Tattoo Artist needs a personal business card designed

I am looking for a classy, clean, but antique feeling business card for myself that matches the theme and vibe of my tattoo shop. I would like to see a couple different options but we can go with an all black background, to start. I would like to see some western metallic lettering and deep/dark red accents. Maybe try adding a few with a mix of white fonts too. I would like to see the Shop's name and location which is Copper Lantern Ink, 4862 W. Delmora Rd. Tampa FL. 33617 Our tattoo shop has a western antique vibe, yet its classy and professional. We have a website you can see the color scheme and grab anymore information for designing this business card from: www.copperlanternink-studio.example - and if you want to add the website to the card. I would like my personal IG handle somewhere small with a unique and cleaner IG logo next to the name. My IG handle is: @dianekessoink I am basically trying to look for multiple ideas/concepts that will match best with our website and sticker. (Which I will upload in the files) I would like it to be very clean, simple, classy, but have a western traditional tattooing feel to it. Like an antique stores business card. Add whatever information you think would be best, since I am not the professional graphic designer.
Shop Name: Copper Lantern Ink
Location: 4862 W Delmora Rd Tampa FL 33617
Website: www.copperlanternink-studio.example
Number: 813 555 0187
My Personal IG: @dianekessoink

Thank you for taking your time to help me out with this project. Afterwards, I might need our studios website up for re-designing! So my end goal is to make everything intergraded with one another. I more likely need a logo too.

Target Market(s)

Professionals 35-55 years of age Male and Female
Firefighters, Military Service men and women

Contact Information for Business Card

All black background, with golden and red accents.
Traditional style, cowboy, western. Sharp, Clean, and Classy.

Requirements
Must have
• Shop Name - Copper Lantern Ink
• Shop Location - 4862 W Delmora Rd Tampa FL 33617
• My Name - Diane Kesso
• UNIQUE IG LOGO along with My Instagram - @dianekessoink
• Number - 813 555 0187
Nice to have
• Gold metallic font
• Red accents
• Western Antique Oddity feel
• Might be nice to have the Website if it can work and fit in the space.

```html
<!DOCTYPE html>
<html lang="en">
<head>
<meta charset="utf-8">
<title>Copper Lantern Ink – Business Card</title>
<link rel="stylesheet" href="https://fonts.googleapis.com/css2?family=Rye&family=Crimson+Text:wght@400;600&display=swap">
<style>
  :root {
    --page: #e9e4dc;
    --card: #0a0808;
    --gold: #c9a84a;
    --gold-soft: #a88a3a;
    --red: #b3202a;
    --red-deep: #8e1820;
    --white: #f4f1ea;
  }
  * { box-sizing: border-box; margin: 0; padding: 0; }
  html, body {
    width: 1200px; height: 780px; overflow: hidden;
    background: var(--page);
  }
  .sheet {
    position: relative; width: 1200px; height: 780px;
    display: flex; align-items: center; justify-content: center; gap: 24px;
  }
  .card {
    position: relative; width: 560px; height: 320px;
    background: var(--card);
    box-shadow: 0 6px 18px rgba(0,0,0,.25);
    overflow: hidden;
  }
  .frame { position: absolute; pointer-events: none; }

  /* Front card */
  .front .frame-outer { inset: 14px; border: 3px double var(--gold); }
  .front .frame-inner { inset: 30px; border: 1px solid var(--red); }
  .front .filigree { background: var(--red-deep); opacity: .85; }
  .front .fleur { background: var(--gold); }

  /* Back card */
  .back .frame-outer { inset: 14px; border: 3px double var(--red); }
  .back .frame-inner { inset: 30px; border: 1px solid var(--gold); }
  .back .filigree { background: var(--gold-soft); opacity: .85; }
  .back .fleur { background: var(--red); }

  .filigree { position: absolute; width: 74px; height: 34px; border-radius: 4px; }
  .filigree.tl { top: 36px; left: 36px; }
  .filigree.tr { top: 36px; right: 36px; }
  .filigree.bl { bottom: 36px; left: 36px; }
  .filigree.br { bottom: 36px; right: 36px; }

  .fleur { position: absolute; width: 18px; height: 18px; border-radius: 50%; }
  .fleur.tl { top: 6px; left: 6px; }
  .fleur.tr { top: 6px; right: 6px; }
  .fleur.bl { bottom: 6px; left: 6px; }
  .fleur.br { bottom: 6px; right: 6px; }

  .contact {
    position: absolute; inset: 0;
    display: flex; flex-direction: column; align-items: center; justify-content: center;
    text-align: center;
    font-family: "Crimson Text", Georgia, serif;
  }
  .contact .name {
    font-family: "Rye", Georgia, serif;
    color: var(--gold); font-size: 28px; letter-spacing: .5px; line-height: 1.1;
  }
  .contact .role { color: var(--red); font-size: 18px; line-height: 1.1; margin-bottom: 14px; }
  .contact .line {
    color: var(--white); font-size: 15px; line-height: 1.45;
    display: flex; align-items: center; justify-content: center; gap: 6px;
  }
  .contact .label { color: var(--gold); }
  .contact .accent { color: var(--red); }
  .contact .ig-mark {
    width: 11px; height: 11px; border: 1.5px solid var(--gold);
    border-radius: 50%; flex: none;
  }

  .brand {
    position: absolute; inset: 0;
    display: flex; flex-direction: column; align-items: center; justify-content: center;
    font-family: "Rye", Georgia, serif; color: var(--gold);
    text-align: center;
  }
  .brand .shop-name { font-size: 40px; line-height: 1.1; letter-spacing: 1px; }
  .brand .shop-city { font-size: 14px; letter-spacing: 3px; margin-top: 10px; }
</style>
</head>
<body>
<main class="sheet">

  <section class="card front">
    <div class="frame frame-outer"></div>
    <div class="frame frame-inner"></div>
    <span class="fleur tl" role="img" aria-label="Gold corner flourish"></span>
    <span class="fleur tr" role="img" aria-label="Gold corner flourish"></span>
    <span class="fleur bl" role="img" aria-label="Gold corner flourish"></span>
    <span class="fleur br" role="img" aria-label="Gold corner flourish"></span>
    <span class="filigree tl" role="img" aria-label="Red scrollwork filigree"></span>
    <span class="filigree tr" role="img" aria-label="Red scrollwork filigree"></span>
    <span class="filigree bl" role="img" aria-label="Red scrollwork filigree"></span>
    <span class="filigree br" role="img" aria-label="Red scrollwork filigree"></span>

    <div class="contact">
      <p class="name">Diane Kesso</p>
      <p class="role">owner</p>
      <p class="line"><span class="label">Phone:</span> 813 555 0187</p>
      <p class="line"><span class="ig-mark" aria-hidden="true"></span><span class="label">Personal IG:</span> @dianekessoink</p>
      <p class="line"><span>www.<span class="accent">copperlanternink-studio</span>.example</span></p>
      <p class="line">4862 W Delmora Rd, Tampa FL 33617</p>
    </div>
  </section>

  <section class="card back">
    <div class="frame frame-outer"></div>
    <div class="frame frame-inner"></div>
    <span class="fleur tl" role="img" aria-label="Red corner flourish"></span>
    <span class="fleur tr" role="img" aria-label="Red corner flourish"></span>
    <span class="fleur bl" role="img" aria-label="Red corner flourish"></span>
    <span class="fleur br" role="img" aria-label="Red corner flourish"></span>
    <span class="filigree tl" role="img" aria-label="Gold scrollwork filigree"></span>
    <span class="filigree tr" role="img" aria-label="Gold scrollwork filigree"></span>
    <span class="filigree bl" role="img" aria-label="Gold scrollwork filigree"></span>
    <span class="filigree br" role="img" aria-label="Gold scrollwork filigree"></span>

    <div class="brand">
      <p class="shop-name">Copper Lantern Ink</p>
      <p class="shop-city">TAMPA, FL</p>
    </div>
  </section>

</main>
</body>
</html>
```